Health and Safety Consultant to the In the renewables wind farm construction industry (OFFSHORE WIND/OIL AND GAS)
APPOINTED PERSON HEAVY LIFTING OPERATIONS.
Lift plan preperations
marcus_dellow@brightmail.example
Tel 07712948305
14 GLANMORE AVE, TALLOWSHIRE NORTH WALES
LL93 4QX
APPOINTED PERSON HEAVY LIFTING OPERATIONS.Health and Safety Consultant to the In the renewables wind farm construction industry (OFFSHORE WIND/OIL AND GAS)

Target Market(s)

Offshore professionals

Industry/Entity Type

Construction

Contact Information for Business Card

M.D.HEALTH AND SAFETY SERVICES LTD
Tel 07712948305
14 Glanmore Ave, Tallowshire West Marches ll934qx

Font styles to use
Serif
Sans Serif

Requirements
Must have
• HIGH QUALITY PLASTIC OR SIMILAR MATERIALS USED
Nice to have
• QUALITY LOGO I HAVE ATTACHED A LOGO BELOW BUT I'M OPENT TO DESIGN CHANGE

```html
<!DOCTYPE html>
<html lang="en">
<head>
<meta charset="utf-8">
<title>M.D. Health and Safety Services – Business Card</title>
<link rel="stylesheet" href="https://fonts.googleapis.com/css2?family=Hind:wght@300;400;500&display=swap">
<style>
  :root {
    --backdrop: #cbd0d0;
    --card: #000000;
    --accent: #2fa4d6;
    --ink: #f2f2f2;
    --muted: #cfcfcf;
  }
  * { box-sizing: border-box; margin: 0; padding: 0; }
  html, body { width: 1200px; height: 823px; overflow: hidden; }
  body {
    background: var(--backdrop);
    font-family: "Hind", Arial, sans-serif;
    position: relative;
  }
  .card {
    position: absolute;
    width: 540px;
    height: 340px;
    background: var(--card);
    box-shadow: 0 6px 18px rgba(0,0,0,0.25);
    overflow: hidden;
  }
  .card--front { left: 40px; top: 300px; }
  .card--back { left: 620px; top: 160px; }

  /* front */
  .accent-bar {
    position: absolute;
    left: 44px;
    width: 7px;
    background: var(--accent);
  }
  .accent-bar--top { top: 0; height: 122px; }
  .accent-bar--bottom { top: 280px; height: 60px; }

  .contact { position: absolute; left: 60px; top: 128px; color: var(--ink); }
  .contact__name {
    font-weight: 300;
    font-size: 30px;
    letter-spacing: 4px;
    line-height: 1;
    text-transform: uppercase;
  }
  .contact__name .surname { color: var(--accent); }
  .contact__role {
    font-weight: 300;
    font-size: 17px;
    letter-spacing: 2px;
    text-transform: uppercase;
    color: var(--muted);
    margin-top: 4px;
  }
  .contact__list { list-style: none; margin-top: 6px; font-size: 16px; line-height: 1.25; }
  .contact__list li { display: flex; align-items: flex-start; gap: 8px; }
  .contact__list svg { width: 11px; height: 11px; margin-top: 3px; flex: none; }
  .icon-fill { fill: var(--accent); }
  .icon-line { fill: none; stroke: var(--accent); stroke-width: 2.5; }

  /* company name */
  .company {
    position: absolute;
    display: flex;
    align-items: center;
    gap: 8px;
    color: var(--accent);
    font-weight: 500;
    letter-spacing: 1px;
    white-space: nowrap;
  }
  .company__mark {
    width: 9px;
    height: 9px;
    background: var(--accent);
    flex: none;
  }
  .card--front .company { right: 36px; top: 62px; font-size: 17px; }
  .card--back .company {
    left: 50%; top: 128px;
    transform: translateX(-50%);
    font-size: 21px;
  }

  /* back */
  .tagline {
    position: absolute;
    left: 0; right: 0; top: 258px;
    display: flex; align-items: center; gap: 14px;
    color: var(--muted);
    font-size: 12px;
    letter-spacing: 2.5px;
    text-transform: uppercase;
  }
  .tagline::before, .tagline::after {
    content: "";
    flex: 1;
    height: 1px;
    background: var(--accent);
    opacity: 0.7;
  }
</style>
</head>
<body>

<section class="card card--back" aria-label="Business card back">
  <p class="company"><span class="company__mark"></span>M.D. Health and Safety Services Ltd</p>
  <p class="tagline">Lift Plan Preperations</p>
</section>

<section class="card card--front" aria-label="Business card front">
  <span class="accent-bar accent-bar--top"></span>
  <span class="accent-bar accent-bar--bottom"></span>

  <p class="company"><span class="company__mark"></span>M.D. Health and Safety Services Ltd</p>

  <div class="contact">
    <h1 class="contact__name">Marcus <span class="surname">Dellow</span></h1>
    <p class="contact__role">Manager</p>
    <ul class="contact__list">
      <li>
        <svg viewBox="0 0 24 24" aria-hidden="true"><path class="icon-fill" d="M6.6 10.8a15.1 15.1 0 0 0 6.6 6.6l2.2-2.2a1 1 0 0 1 1-.25 11.4 11.4 0 0 0 3.6.57 1 1 0 0 1 1 1V20a1 1 0 0 1-1 1A17 17 0 0 1 3 4a1 1 0 0 1 1-1h3.5a1 1 0 0 1 1 1c0 1.25.2 2.45.57 3.57a1 1 0 0 1-.25 1z"/></svg>
        <span>07712948305</span>
      </li>
      <li>
        <svg viewBox="0 0 24 24" aria-hidden="true"><path class="icon-line" d="M3 6h18v12H3z M3 6l9 7 9-7"/></svg>
        <span>marcus_dellow@brightmail.example</span>
      </li>
      <li>
        <svg viewBox="0 0 24 24" aria-hidden="true"><path class="icon-fill" d="M12 2a7 7 0 0 0-7 7c0 5.2 7 13 7 13s7-7.8 7-13a7 7 0 0 0-7-7zm0 9.5A2.5 2.5 0 1 1 12 6.5a2.5 2.5 0 0 1 0 5z"/></svg>
        <span>14 Glanmore Ave,<br>Tallowshire West Marches ll934qx</span>
      </li>
    </ul>
  </div>
</section>

</body>
</html>
```